Silicone cotton stick need a packaging design and logo and product images

Make a visual identity for the brand, a logo and packaging for the product silicone cotton swab and product images to sell on Zorvane Bazaar with 6 images. packaging a maximum of 4 colors should capture attention, and inspire safety and environmental preservation. product images size min 3000 x 3000. Example: https: //plumtiq.example/collections/eco-friendly-ear-swab/products/plumtiq-grey-owl-tip

Target Market(s)

Women

Industry/Entity Type

Beauty

Logo Text

quelmora

Font styles to use
Sans Serif

Colors

Designer to choose colors to be used in the design.

Requirements
Must have
• A logo with on color, a packaging design with the template provided. The logo is written on the plastic box in on color it takes, 6 images product to sell on marketplace zorvane, see an example on zorvane with the following link https://www.zorvane.example/Reutilisable-Item-Eco / dp / Q48HHTR2MN / ref = sr_1_7 ? crid = 8KQPLWXJ31T2A% 26amp; keywords = + stem + cotton reusable% 26amp; qid = 1290384756; sr = 8-7
Should not have
• Not copying others, something original and effective, capture attention impotent

```html
<!DOCTYPE html>
<html lang="en">
<head>
<meta charset="utf-8">
<title>Quelmora Reusable Silicone Swabs – Packaging</title>
<link href="https://fonts.googleapis.com/css2?family=Montserrat:wght@300;400;500&display=swap" rel="stylesheet">
<style>
  :root {
    --teal-light: #3fbcb1;
    --teal: #1aa89c;
    --teal-deep: #12968b;
    --taupe-light: #a89a8f;
    --taupe: #8e7a6d;
    --taupe-deep: #7f6b5e;
    --green: #37a647;
    --green-light: #4cb75a;
    --white: #ffffff;
    --ink: #1d1d1d;
    --window: #3c3d45;
    --bg: #efefef;
  }
  * { margin: 0; padding: 0; box-sizing: border-box; }
  html, body { width: 1200px; height: 1080px; overflow: hidden; }
  body {
    background: var(--bg);
    font-family: "Montserrat", sans-serif;
    position: relative;
  }
  .box { position: absolute; top: 110px; height: 860px; display: flex; }
  .box--left { left: 130px; }
  .box--right { left: 640px; }

  .panel { position: relative; height: 100%; overflow: hidden; }
  .panel--side { width: 100px; }
  .panel--front { width: 340px; }

  .zone { position: absolute; left: 0; right: 0; }
  .zone--top { top: 0; height: 160px; }
  .zone--body { top: 160px; height: 590px; }
  .zone--base { top: 750px; height: 110px; }
  .panel--front .zone--base { overflow: visible; }
  .panel--front { overflow: visible; }

  .panel--side .zone--top { background: var(--teal-deep); }
  .panel--side .zone--body { background: var(--taupe-deep); }
  .panel--side .zone--base { background: var(--green); }

  .panel--front .zone--top { background: linear-gradient(120deg, var(--teal-light), var(--teal) 55%, var(--teal-deep)); }
  .panel--front .zone--body { background: linear-gradient(90deg, var(--taupe-light), var(--taupe) 55%, var(--taupe-deep)); }
  .panel--front .zone--base { background: linear-gradient(90deg, var(--green-light), var(--green)); }

  .wordmark {
    position: absolute; top: 52px; left: 0; right: 0;
    text-align: center; color: var(--white);
    font-weight: 300; font-size: 44px; letter-spacing: 0.5px;
  }

  .side-text {
    position: absolute; top: 180px; left: 0; right: 0; height: 560px;
    display: flex; align-items: center; justify-content: center; gap: 34px;
    writing-mode: vertical-rl; color: var(--ink);
    font-size: 28px; letter-spacing: 1.5px; white-space: nowrap;
  }
  .side-text--up { transform: rotate(180deg); }
  .side-text .brand { font-weight: 300; }
  .side-text .label { font-weight: 400; }

  .swab-art {
    position: absolute; top: 36px; left: 60px; width: 220px; height: 510px;
    background: linear-gradient(180deg, rgba(255,255,255,0.22), rgba(255,255,255,0.12));
    border-radius: 14px;
  }

  .window {
    position: absolute; top: 172px; left: 135px;
    width: 70px; height: 70px; border-radius: 50%;
    background: var(--window); border: 2px solid #2a2a30;
  }

  .name-band {
    position: absolute; top: 296px; left: 0; right: 0; height: 150px;
    background: linear-gradient(90deg, var(--teal-light), var(--teal-deep));
    border-top: 5px solid var(--white); border-bottom: 5px solid var(--white);
    padding: 14px 0 0 66px;
    color: var(--white); font-size: 30px; font-weight: 400; line-height: 1.22;
  }

  .eco-badge {
    position: absolute; top: -22px; left: 40px;
    width: 262px; height: 112px; border-radius: 56px;
    background: var(--white);
    border: 5px solid var(--green);
    display: flex; align-items: center; padding-left: 10px;
  }
  .eco-badge .seal {
    width: 88px; height: 88px; border-radius: 50%;
    background: var(--green);
  }
</style>
</head>
<body>

  <section class="box box--left" aria-label="Quelmora box, windowed version">
    <div class="panel panel--side">
      <div class="zone zone--top"></div>
      <div class="zone zone--body"></div>
      <div class="zone zone--base"></div>
      <p class="side-text side-text--up"><span class="brand">Quelmora</span><span class="label">Reusable Swabs</span></p>
    </div>
    <div class="panel panel--front">
      <div class="zone zone--top"><h1 class="wordmark">Quelmora</h1></div>
      <div class="zone zone--body">
        <div class="swab-art" role="img" aria-label="Two white silicone swabs, one textured and one with a pointed and a teardrop tip"></div>
        <div class="window"></div>
        <h2 class="name-band">Reusable<br>Silicone<br>Swabs</h2>
      </div>
      <div class="zone zone--base">
        <div class="eco-badge" role="img" aria-label="Eco friendly badge"><span class="seal"></span></div>
      </div>
    </div>
  </section>

  <section class="box box--right" aria-label="Quelmora box, plain version">
    <div class="panel panel--side">
      <div class="zone zone--top"></div>
      <div class="zone zone--body"></div>
      <div class="zone zone--base"></div>
      <p class="side-text"><span class="brand">Quelmora</span><span class="label">Reusable Swabs</span></p>
    </div>
    <div class="panel panel--front">
      <div class="zone zone--top"><h1 class="wordmark">Quelmora</h1></div>
      <div class="zone zone--body">
        <div class="swab-art" role="img" aria-label="Two white silicone swabs, one textured and one with a pointed and a teardrop tip"></div>
      </div>
      <div class="zone zone--base">
        <div class="eco-badge" role="img" aria-label="Eco friendly badge"><span class="seal"></span></div>
      </div>
    </div>
  </section>

</body>
</html>
```